Design of 3 Minimalist Icons

We need icons that depict the following:
- Made in Australia
- Personalisation Option Available
- Orders Ship In 2 Business Days

Our business makes premium wooden toys, with the option of having the child's name and birthdate laser etched onto the toy. See our website, corvelthane.com.au to view the products.

Once completed, we want the icons in AI vector format.

Target Market(s)

Females 25-40 year old who appreciate beautiful, quality products.

Industry/Entity Type

Business

Font styles to use
Sans Serif

Colors
000000
ffffff

Requirements
Must have
• The icons must be:
• - Very simple/minimalist
• - Classy, premium and high-end looking
• - Black and white with a white background
• - Stylistically compatible with our logo (see attachment)
• - Matching in style
• The icons must include their text below in Proxima Nova font. They will be for use on our website.
Should not have
• The 'Ships in 2 Business Days' logo should depict shipping rather than look 'fast'.

```html
<!DOCTYPE html>
<html lang="en">
<head>
<meta charset="utf-8">
<title>Corvelthane — Product Promise Icons</title>
<link rel="stylesheet" href="https://fonts.googleapis.com/css2?family=Exo+2:wght@400&display=swap">
<style>
  :root {
    --ink: #000000;
    --paper: #ffffff;
    --map-tone: #e6e6e6;
  }
  html, body {
    margin: 0;
    padding: 0;
    width: 1200px;
    height: 1200px;
    overflow: hidden;
    background: var(--paper);
  }
  .icon-sheet {
    position: relative;
    width: 1200px;
    height: 1200px;
  }
  .icon-art {
    position: absolute;
    inset: 0;
  }
  .badge-ring {
    fill: none;
    stroke: var(--ink);
    stroke-width: 4;
  }
  .badge-line {
    fill: none;
    stroke: var(--ink);
    stroke-width: 4;
    stroke-linejoin: round;
    stroke-linecap: round;
  }
  .map-placeholder {
    position: absolute;
    left: 488px;
    top: 202px;
    width: 222px;
    height: 198px;
    border-radius: 46% 52% 44% 48%;
    background: var(--map-tone);
  }
  .badge-label {
    position: absolute;
    width: 400px;
    margin: 0;
    text-align: center;
    font-family: "Exo 2", sans-serif;
    font-weight: 400;
    font-size: 30px;
    line-height: 40px;
    color: var(--ink);
    letter-spacing: 0.5px;
  }
  .label-origin { left: 398px; top: 484px; }
  .label-personal { left: 150px; top: 982px; }
  .label-shipping { left: 648px; top: 982px; }
</style>
</head>
<body>
<main class="icon-sheet">
  <svg class="icon-art" width="1200" height="1200" viewBox="0 0 1200 1200" aria-hidden="true">
    <circle class="badge-ring" cx="598" cy="297" r="156"/>
    <circle class="badge-ring" cx="350" cy="796" r="156"/>
    <circle class="badge-ring" cx="848" cy="796" r="156"/>

    <path class="badge-line heart-icon"
      d="M350 749 C325 722 290 716 266 728 C244 740 240 770 250 795 C262 822 310 862 350 900 C390 862 438 822 450 795 C460 770 456 740 434 728 C410 716 375 722 350 749 Z"/>

    <g class="plane-icon" transform="translate(848 796) rotate(45) scale(8.5) translate(-12 -12)">
      <path d="M21 16v-2l-8-5V3.5c0-.83-.67-1.5-1.5-1.5S10 2.67 10 3.5V9l-8 5v2l8-2.5V19l-2 1.5V22l3.5-1 3.5 1v-1.5L13 19v-5.5l8 2.5z"
        fill="none" stroke="#000" stroke-width="0.47" stroke-linejoin="round"/>
    </g>
  </svg>

  <div class="map-placeholder" role="img" aria-label="Outline map of Australia with Tasmania"></div>

  <p class="badge-label label-origin">Made In<br>Australia</p>
  <p class="badge-label label-personal">Personalisation<br>Option Available</p>
  <p class="badge-label label-shipping">Order Ship<br>In 2 Business Days</p>
</main>
</body>
</html>
```